Business Card Design for Orthopaedic Surgeon

This is a double-sided glossy business card. I prefer baby blue, teal, and green as color schemes. I have my logo already (many colors that you can choose from). I have photos and examples of my old card (very bland but has the information in it). I also have one that my assistant tried to design, but the writing is too small and I don't love the formatting. But it is close!
I would like my logo to be on the business card but I'm uploading my logo in many different colors so you can choose which one looks best based on the color scheme. I also uploaded many sized headshots so you can choose the best resolution one.

Additional information:
Correct business address:
4382 NW 58th Lane, Suite 305
Tamarac, FL 33417

Everything else on both business cards are accurate.

I actually need 2 different business cards generated. One that includes my cell phone number-- Personal cell: 585-314-9062 in addition to Office phone: (954) 316-4870 and Office Fax: 954-316-4881. Again, one card would have my personal cell and one wouldn't

Overall I just think the baby blue card (uploaded) is missing something on the front--of course it is also missing my office phone/fax/personal cell. I do want my website on the front too. Email: info@wellsorthocare.example

You can use your discretion about what goes on the front vs. what goes on the back to eliminated clutter.

Oh and on the back, I would like to list "Conditions Treated" (not specialties include). The list is:
Carpal Tunnel
Trigger Finger
Ganglion Cysts
Hand Tumors
Han & Wrist Arthritis
Hand, Wrist & Elbow Tendonitis
Fractures of the Hand, Wrist, Elbow and Humerus
Nerve Injuries of the Hand, Wrist & Elbow
Microsurgery
Wrist Arthroscopy
Endoscopic Surgery

Target Market(s)

Primary care doctors, Lawyers, patients

Industry/Entity Type

Medical

Contact Information for Business Card

Please see above in project description

Colors

Designer to choose colors to be used in the design.

Requirements
Must have
• -Correct office info, Board Certified Orthopaedic Hand & Upper Extremity Surgeon
Nice to have
• Something that is classy and wow!

```html
<!DOCTYPE html>
<html lang="en">
<head>
<meta charset="utf-8">
<title>Renata Wells, MD – Business Card</title>
<link href="https://fonts.googleapis.com/css2?family=Poppins:wght@400;500;600&display=swap" rel="stylesheet">
<style>
  :root {
    --teal: #00858a;
    --ink: #1f1f1f;
    --card-dark: #212121;
    --paper: #ffffff;
    --backdrop: #a3a3a3;
    --light-text: #f2f2f2;
  }
  * { margin: 0; padding: 0; box-sizing: border-box; }
  html, body { width: 1093px; height: 1200px; overflow: hidden; }
  body {
    background: var(--backdrop);
    font-family: "Poppins", sans-serif;
    position: relative;
  }
  .card {
    position: absolute;
    left: 265px;
    width: 580px;
    height: 356px;
    border-radius: 26px;
    overflow: hidden;
  }
  /* Front */
  .card-front { top: 226px; background: var(--paper); color: var(--ink); }
  .portrait {
    position: absolute; right: 0; top: 0; width: 232px; height: 356px;
    background:
      linear-gradient(to right, #ffffff 0%, rgba(255,255,255,0) 22%),
      radial-gradient(ellipse 55% 40% at 52% 38%, #8a5a40 0%, #5a3a2c 45%, rgba(40,32,30,0.9) 75%, rgba(255,255,255,0) 100%),
      linear-gradient(to bottom, #ffffff 0%, #ffffff 55%, #2a2a2a 80%, #1c1c1c 100%);
  }
  .name {
    position: absolute; left: 26px; top: 46px;
    font-size: 22px; line-height: 26px; font-weight: 600; color: var(--teal); letter-spacing: 0.2px;
    white-space: nowrap;
  }
  .title {
    position: absolute; left: 26px; top: 73px;
    font-size: 16px; line-height: 21px; font-weight: 400; white-space: nowrap;
  }
  .rule {
    position: absolute; left: 26px; width: 40px; height: 1.5px; background: var(--teal);
  }
  .rule-top { top: 126px; }
  .rule-bottom { top: 267px; }
  .contact-list {
    position: absolute; left: 26px; top: 147px; list-style: none;
  }
  .contact-list li {
    display: flex; align-items: center; gap: 8px;
    font-size: 17px; line-height: 21px; height: 21px; white-space: nowrap;
  }
  .contact-list svg { width: 15px; height: 15px; flex: none; fill: var(--teal); }
  .address {
    position: absolute; left: 26px; top: 283px;
    font-size: 17px; line-height: 21px; white-space: nowrap;
  }
  /* Back */
  .card-back { top: 621px; background: var(--card-dark); color: var(--light-text); }
  .side-band {
    position: absolute; left: 0; top: 0; width: 77px; height: 356px; background: var(--teal);
  }
  .side-band-notch { position: absolute; left: 76px; top: 168px; }
  .side-label {
    position: absolute; left: 38px; top: 178px;
    transform: translate(-50%, -50%) rotate(-90deg);
    white-space: nowrap;
    font-size: 18px; font-weight: 600; color: #fff; letter-spacing: 0.3px;
  }
  .conditions {
    position: absolute; left: 107px; top: 40px; list-style: none;
  }
  .conditions li {
    position: relative; padding-left: 12px;
    font-size: 15.5px; line-height: 15.5px; margin-bottom: 6.5px; white-space: nowrap;
  }
  .conditions li::before {
    content: ""; position: absolute; left: 0; top: 2px;
    width: 7px; height: 7px; border-radius: 50%; background: var(--teal);
  }
  .brand {
    position: absolute; left: 362px; top: 83px; width: 192px; height: 192px;
    border: 4px solid var(--teal); border-radius: 50%;
    display: flex; align-items: center; justify-content: center;
  }
  .brand-name {
    font-size: 24px; font-weight: 600; color: var(--teal); letter-spacing: 1px;
  }
</style>
</head>
<body>

<section class="card card-front">
  <div class="portrait" role="img" aria-label="Headshot of the surgeon in a dark blazer and white blouse on a white background"></div>
  <h1 class="name">RENATA WELLS, MD</h1>
  <p class="title">Board Certified Orthopaedic Hand &amp;<br>Upper Extremity Surgeon</p>
  <div class="rule rule-top"></div>
  <ul class="contact-list">
    <li><svg viewBox="0 0 24 24"><path d="M6.6 10.8a15.1 15.1 0 0 0 6.6 6.6l2.2-2.2c.3-.3.7-.4 1-.2 1.1.4 2.3.6 3.6.6.6 0 1 .4 1 1V20c0 .6-.4 1-1 1A17 17 0 0 1 3 4c0-.6.4-1 1-1h3.5c.6 0 1 .4 1 1 0 1.3.2 2.5.6 3.6.1.3 0 .7-.2 1z"/></svg>585-314-9062</li>
    <li><svg viewBox="0 0 24 24"><path d="M7 1h10a2 2 0 0 1 2 2v18a2 2 0 0 1-2 2H7a2 2 0 0 1-2-2V3a2 2 0 0 1 2-2zm0 3v14h10V4z"/></svg>(954) 316-4870</li>
    <li><svg viewBox="0 0 24 24"><path d="M6 2h12v5H6zM3 8h18a2 2 0 0 1 2 2v7h-4v5H5v-5H1v-7a2 2 0 0 1 2-2zm4 7v5h10v-5z"/></svg>954-316-4881</li>
    <li><svg viewBox="0 0 24 24"><path d="M2 5h20v14H2zm2 2v.5l8 5 8-5V7l-8 5z"/></svg>info@wellsorthocare.example</li>
    <li><svg viewBox="0 0 24 24"><path d="M12 2a10 10 0 1 0 0 20 10 10 0 0 0 0-20zm6.9 6h-3a15 15 0 0 0-1.3-3.9A8 8 0 0 1 18.9 8zM12 4c.8 1.1 1.5 2.5 1.9 4h-3.8c.4-1.5 1.1-2.9 1.9-4zM4.3 14a8 8 0 0 1 0-4h3.4a16 16 0 0 0 0 4zm.8 2h3a15 15 0 0 0 1.3 3.9A8 8 0 0 1 5.1 16zm3-8h-3a8 8 0 0 1 4.3-3.9A15 15 0 0 0 8.1 8zM12 20c-.8-1.1-1.5-2.5-1.9-4h3.8c-.4 1.5-1.1 2.9-1.9 4zm2.3-6H9.7a14 14 0 0 1 0-4h4.6a14 14 0 0 1 0 4zm.3 5.9a15 15 0 0 0 1.3-3.9h3a8 8 0 0 1-4.3 3.9zm1.7-5.9a16 16 0 0 0 0-4h3.4a8 8 0 0 1 0 4z"/></svg>www.wellsorthocare.example</li>
  </ul>
  <div class="rule rule-bottom"></div>
  <p class="address">4382 NW 58th Lane, Suite 305<br>Tamarac, FL 33417</p>
</section>

<section class="card card-back">
  <div class="side-band"></div>
  <svg class="side-band-notch" width="14" height="20" viewBox="0 0 14 20"><path d="M0 0 L14 10 L0 20 Z" fill="var(--teal)"/></svg>
  <h2 class="side-label">CONDITIONS TREATED</h2>
  <ul class="conditions">
    <li>Carpal Tunnel</li>
    <li>Trigger Finger</li>
    <li>Ganglion Cysts</li>
    <li>Hand Tumors</li>
    <li>Han &amp; Wrist Arthritis</li>
    <li>Hand, Wrist &amp; Elbow Tendonitis</li>
    <li>Fractures of the Hand<br>Wrist, Elbow and Humerus</li>
    <li>Nerve Injuries of the Hand<br>Wrist &amp; Elbow</li>
    <li>Microsurgery</li>
    <li>Wrist Arthroscopy</li>
    <li>Endoscopic Surgery</li>
  </ul>
  <div class="brand"><span class="brand-name">WELLS HAND</span></div>
</section>

</body>
</html>
```